Business Card design for new private practice opening

I need a business card design for my new private practice with my new logo uploaded as a file
On the front the logo
On the back: maybe a small logo somewhere?
Priv. Doz. DDr. Corinna Vestaluk
Fachärztin für Allgemein- & Viszeralchirurgie
Address: xxx
Tel: xxx
Mobil:xxx
Webseite:xxx
Email:xxx

Contact Information for Business Card

See project description above for details

Requirements
Nice to have
• I would like the colors of the logo incorporated into the business card

```html
<!DOCTYPE html>
<html lang="de">
<head>
<meta charset="utf-8">
<title>Visitenkarte – Priv. Doz. DDr. Corinna Vestaluk</title>
<link rel="stylesheet" href="https://fonts.googleapis.com/css2?family=Montserrat:ital,wght@0,400;0,500;0,600;1,400&display=swap">
<style>
  :root {
    --teal: #4fb3ad;
    --grey: #7f7f7f;
    --grey-dark: #555555;
    --paper: #ffffff;
    --backdrop: #ececec;
  }
  * { box-sizing: border-box; margin: 0; padding: 0; }
  html, body {
    width: 1200px; height: 509px; overflow: hidden;
    background: var(--backdrop);
    font-family: "Montserrat", Arial, sans-serif;
  }
  .canvas { position: relative; width: 1200px; height: 509px; }
  .card {
    position: absolute; top: 84px; width: 527px; height: 343px;
    background: var(--paper);
  }
  .card--front { left: 40px; }
  .card--back { left: 649px; }
  .card__frame { position: absolute; pointer-events: none; }
  .card--front .card__frame { inset: 17px 18px; border: 2px solid var(--teal); }
  .card--back .card__frame { inset: 14px 14px; border: 1.5px solid var(--grey); }

  .brand {
    position: absolute; left: 0; right: 0;
    display: flex; align-items: center; justify-content: center;
    color: var(--teal); font-weight: 600;
  }
  .brand__circle { border-radius: 50%; border: 4px solid var(--grey); flex: none; }
  .card--front .brand { top: 131px; gap: 18px; font-size: 30px; }
  .card--front .brand__circle { width: 80px; height: 80px; border-width: 5px; }
  .card--back .brand { top: 58px; gap: 10px; font-size: 17px; }
  .card--back .brand__circle { width: 44px; height: 44px; border-width: 3px; }

  .identity { position: absolute; top: 140px; left: 0; right: 0; text-align: center; color: var(--grey); }
  .identity__name { font-size: 23.5px; font-weight: 600; letter-spacing: 0.1px; }
  .identity__title { margin-top: 3px; font-size: 15.5px; font-style: italic; color: var(--grey-dark); }

  .contact { position: absolute; top: 208px; left: 84px; list-style: none; color: var(--grey-dark); font-size: 15.5px; }
  .contact__row { display: flex; align-items: center; height: 21.6px; }
  .contact__icon { width: 15px; height: 15px; margin-right: 6px; fill: var(--grey); flex: none; }
  .contact__label { width: 94px; }
</style>
</head>
<body>
<div class="canvas">
  <section class="card card--front">
    <div class="card__frame"></div>
    <div class="brand"><span class="brand__circle"></span><span class="brand__name">Praxis Vestaluk</span></div>
  </section>

  <section class="card card--back">
    <div class="card__frame"></div>
    <div class="brand"><span class="brand__circle"></span><span class="brand__name">Praxis Vestaluk</span></div>
    <div class="identity">
      <h1 class="identity__name">Priv. Doz. DDr. Corinna Vestaluk</h1>
      <p class="identity__title">Fachärztin für Allgemein- &amp; Viszeralchirurgie</p>
    </div>
    <ul class="contact">
      <li class="contact__row">
        <svg class="contact__icon" viewBox="0 0 16 16"><path d="M8 1a5 5 0 0 0-5 5c0 3.6 5 9 5 9s5-5.4 5-9a5 5 0 0 0-5-5zm0 7a2 2 0 1 1 0-4 2 2 0 0 1 0 4z"/></svg>
        <span class="contact__label">Address:</span><span>Lerchengasse 48, 1080 Wien</span>
      </li>
      <li class="contact__row">
        <svg class="contact__icon" viewBox="0 0 16 16"><path d="M3.6 1.5l2.3 2.6-1.2 1.8c.8 1.9 2.4 3.5 4.3 4.4l1.8-1.2 2.6 2.3-1.3 2.3C7 13.5 2.5 9 2.3 2.8z"/></svg>
        <span class="contact__label">Tel:</span><span>+43 1 408 2917</span>
      </li>
      <li class="contact__row">
        <svg class="contact__icon" viewBox="0 0 16 16"><path d="M5 1h6a1 1 0 0 1 1 1v12a1 1 0 0 1-1 1H5a1 1 0 0 1-1-1V2a1 1 0 0 1 1-1zm.5 1.5v9.5h5V2.5zM8 12.8a.7.7 0 1 0 0 1.4.7.7 0 0 0 0-1.4z"/></svg>
        <span class="contact__label">Mobil:</span><span>+43 664 583 2046</span>
      </li>
      <li class="contact__row">
        <svg class="contact__icon" viewBox="0 0 16 16"><path d="M8 1a7 7 0 1 0 0 14A7 7 0 0 0 8 1zm5.4 6.3h-2.5a11 11 0 0 0-1-4.4 5.6 5.6 0 0 1 3.5 4.4zM8 2.5c.7.9 1.3 2.6 1.5 4.8h-3C6.7 5.1 7.3 3.4 8 2.5zM6.1 2.9a11 11 0 0 0-1 4.4H2.6a5.6 5.6 0 0 1 3.5-4.4zM2.6 8.7h2.5a11 11 0 0 0 1 4.4 5.6 5.6 0 0 1-3.5-4.4zM8 13.5c-.7-.9-1.3-2.6-1.5-4.8h3c-.2 2.2-.8 3.9-1.5 4.8zm1.9-.4a11 11 0 0 0 1-4.4h2.5a5.6 5.6 0 0 1-3.5 4.4z"/></svg>
        <span class="contact__label">Webseite:</span><span>www.praxis-vestaluk.at</span>
      </li>
      <li class="contact__row">
        <svg class="contact__icon" viewBox="0 0 16 16"><path d="M1.5 3.5h13v9h-13zm1.2 1.1v.3L8 8.6l5.3-3.7v-.3zm0 1.7v5.1h10.6V6.3L8 10z"/></svg>
        <span class="contact__label">Email:</span><span>ordination@praxis-vestaluk.at</span>
      </li>
    </ul>
  </section>
</div>
</body>
</html>
```